Wedding Day Custom Wine Label - Tasmanian (Tamar Valley) wine

I am looking for a custom design that will be put on a wine label to commemorate a very good friend's wedding day.

We will need to be able to take the design and print it on to sticker labels that we can put on to wine bottles.

The bride and groom have asked for a simplistic label design (see example image attached). We need two labels. One for "Pinot Noir" wine and the other for "Chardonnay" wine. We would like the label to say:

The Drumwell's
Pinot Noir
2023
Tamar Valley

and for for the other wine variety:

The Drumwell's
Chardonnay
2023
Tamar Valley

smaller text below to say:

13.5% ALC/VOL 750ML
MAREN & JONAS - 31.10.2024

I am happy to consider other variations - the bride & groom would prefer something minimalistic. Elegant and classy.

Target Market(s)

the bride & groom

Requirements
Must have
• Wedding date (31.10.2024). Wine type (Pinot Noir or Chardonnay).
Should not have
• images not essential

```html
<!DOCTYPE html>
<html lang="en">
<head>
<meta charset="UTF-8">
<title>The Drumwell's Wedding Wine Labels</title>
<link rel="stylesheet" href="https://fonts.googleapis.com/css2?family=Poppins:wght@500;600&display=swap">
<style>
  :root {
    --ink: #000000;
    --paper: #ffffff;
  }
  * { margin: 0; padding: 0; box-sizing: border-box; }
  html, body {
    width: 1200px;
    height: 1200px;
    overflow: hidden;
    background: var(--paper);
  }
  .sheet {
    position: relative;
    width: 1200px;
    height: 1200px;
    font-family: "Poppins", sans-serif;
    color: var(--ink);
  }
  .dark-band {
    position: absolute;
    left: 0;
    top: 632px;
    width: 1200px;
    height: 568px;
    background: var(--ink);
  }
  .label {
    position: absolute;
    width: 347px;
    height: 396px;
    background: var(--paper);
  }
  .label--outlined { border: 2px solid var(--ink); }
  .label--left { left: 187px; }
  .label--right { left: 682px; }
  .label--top { top: 108px; }
  .label--bottom { top: 718px; }

  .label__line {
    position: absolute;
    left: 0;
    width: 100%;
    text-align: center;
    line-height: 1;
    transform: translateY(-50%);
    white-space: nowrap;
  }
  .label__estate,
  .label__variety,
  .label__region {
    font-size: 29px;
    font-weight: 600;
    letter-spacing: 0.2px;
  }
  .label__vintage {
    font-size: 29px;
    font-weight: 600;
    letter-spacing: 7px;
    text-indent: 7px;
  }
  .label__estate { top: 81px; }
  .label__variety { top: 153px; }
  .label__vintage { top: 188px; }
  .label__region { top: 219px; }

  .label__rule {
    position: absolute;
    left: 105px;
    top: 263px;
    width: 137px;
    height: 4px;
    background: var(--ink);
  }
  .label__detail {
    font-size: 15.5px;
    font-weight: 600;
  }
  .label__detail--abv { top: 302px; }
  .label__detail--couple { top: 326px; }
</style>
</head>
<body>
<main class="sheet">
  <div class="dark-band"></div>

  <section class="label label--outlined label--left label--top">
    <p class="label__line label__estate">THE DRUMWELL’S</p>
    <p class="label__line label__variety">PINOT NOIR</p>
    <p class="label__line label__vintage">2023</p>
    <p class="label__line label__region">TAMAR VALLEY</p>
    <div class="label__rule"></div>
    <p class="label__line label__detail label__detail--abv">13.5% ALC/VOL 750ML</p>
    <p class="label__line label__detail label__detail--couple">MAREN &amp; JONAS – 31.10.2024</p>
  </section>

  <section class="label label--outlined label--right label--top">
    <p class="label__line label__estate">THE DRUMWELL’S</p>
    <p class="label__line label__variety">CHARDONNAY</p>
    <p class="label__line label__vintage">2023</p>
    <p class="label__line label__region">TAMAR VALLEY</p>
    <div class="label__rule"></div>
    <p class="label__line label__detail label__detail--abv">13.5% ALC/VOL 750ML</p>
    <p class="label__line label__detail label__detail--couple">MAREN &amp; JONAS – 31.10.2024</p>
  </section>

  <section class="label label--left label--bottom">
    <p class="label__line label__estate">THE DRUMWELL’S</p>
    <p class="label__line label__variety">PINOT NOIR</p>
    <p class="label__line label__vintage">2023</p>
    <p class="label__line label__region">TAMAR VALLEY</p>
    <div class="label__rule"></div>
    <p class="label__line label__detail label__detail--abv">13.5% ALC/VOL 750ML</p>
    <p class="label__line label__detail label__detail--couple">MAREN &amp; JONAS – 31.10.2024</p>
  </section>

  <section class="label label--right label--bottom">
    <p class="label__line label__estate">THE DRUMWELL’S</p>
    <p class="label__line label__variety">CHARDONNAY</p>
    <p class="label__line label__vintage">2023</p>
    <p class="label__line label__region">TAMAR VALLEY</p>
    <div class="label__rule"></div>
    <p class="label__line label__detail label__detail--abv">13.5% ALC/VOL 750ML</p>
    <p class="label__line label__detail label__detail--couple">MAREN &amp; JONAS – 31.10.2024</p>
  </section>
</main>
</body>
</html>
```